Updated Stationary needed using new logo for Hair Tissue Mineral Analysis Company

Simple stationary design needed using new logo!
1. 8.5" x 11" Letterhead with company information listed below
2. 8.5" x 11" Design with Footer only with logo and information for print materials
3. 5.5" x 8.5" letterhead design
4. 4.125" x 9.5" Business envelope (#10 envelope) with address
5. 4.125" x 9.5" Business envelope with clear window (#10 envelope) with address
6. 6.5" x 9.5" envelope (6 3/4 Booklet envelope) with address
7. 10" x 13" Open End envelope
Address:
4817 N. Corwin Street
Phoenix, AZ 85021
Phone:
(602)-417-3926
Website:
www.pexumor.com
Email:
information@pexumor.com
Updates
Need extra days to review
Focused on completing other projects first
Look and feel
Each slider illustrates characteristics of the customer's brand and the style your logo design should communicate.

```html
<!DOCTYPE html>
<html lang="en">
<head>
<meta charset="utf-8">
<title>Pexumor Labs Stationery</title>
<link rel="stylesheet" href="https://fonts.googleapis.com/css2?family=Arimo:wght@400;700&display=swap">
<style>
  :root {
    --brand-blue: #2f569c;
    --brand-blue-soft: #4a72b8;
    --brand-orange: #f58220;
    --ink: #4a4a4a;
    --paper: #ffffff;
    --backdrop: #c8c8c8;
  }
  html, body {
    margin: 0;
    padding: 0;
    width: 993px;
    height: 1200px;
    overflow: hidden;
    background: var(--backdrop);
    font-family: "Arimo", Arial, sans-serif;
    color: var(--ink);
  }
  .sheet {
    position: absolute;
    background: var(--paper);
    box-shadow: 2px 2px 3px rgba(0,0,0,.35);
    overflow: hidden;
  }
  .header-band {
    position: absolute;
    left: 0;
    top: 0;
    width: 100%;
    background: linear-gradient(90deg, var(--brand-blue) 0%, var(--brand-blue-soft) 100%);
  }
  .header-rule {
    position: absolute;
    left: 0;
    width: 100%;
    height: 2px;
    background: var(--brand-orange);
  }
  .brand {
    position: absolute;
    display: flex;
    align-items: center;
    gap: 0.35em;
    white-space: nowrap;
  }
  .brand-dot {
    width: 0.6em;
    height: 0.6em;
    border-radius: 50%;
    background: var(--brand-orange);
  }
  .brand-name {
    color: var(--brand-blue);
    font-weight: 700;
    letter-spacing: 0.06em;
  }

  /* letterhead */
  .letter { width: 316px; height: 408px; }
  .letter .header-band { height: 18px; }
  .letter .header-rule { top: 18px; }
  .letter .brand { left: 111px; top: 30px; font-size: 12px; }
  .letter-body { position: absolute; left: 32px; top: 120px; width: 252px; }
  .salutation { font-size: 7.4px; margin: 0 0 12px; }
  .paragraph { font-size: 5px; line-height: 6.2px; margin: 0 0 6px; }
  .closing { font-size: 3.8px; margin: 9px 0 8px; }
  .signature { width: 38px; height: 12px; background: linear-gradient(90deg,#e6e6e6,#f2f2f2); }
  .footer {
    position: absolute;
    left: 0; right: 0;
    text-align: center;
  }
  .letter .footer { bottom: 10px; font-size: 5.4px; }
  .footer-address { padding-bottom: 2px; margin: 0 auto; display: inline-block; border-bottom: 0.6px solid var(--brand-orange); width: 166px; }
  .footer-contact { display: flex; justify-content: center; gap: 4px; margin-top: 3px; align-items: center; }
  .contact-item { display: inline-flex; align-items: center; gap: 2px; }
  .icon { width: 1em; height: 1em; fill: var(--brand-orange); }

  /* half letter */
  .half-letter { width: 204px; height: 315px; }
  .half-letter .header-band { height: 12px; }
  .half-letter .header-rule { top: 12px; height: 1.5px; }
  .half-letter .brand { left: 66px; top: 17px; font-size: 7.5px; }
  .half-letter .footer { bottom: 6px; font-size: 3.2px; }
  .half-letter .footer-address { width: 108px; }

  /* envelopes */
  .envelope .header-band { height: 20px; }
  .envelope .header-rule { top: 20px; }
  .envelope .brand { left: 138px; top: 34px; font-size: 16px; }
  .return-address { position: absolute; left: 346px; top: 36px; font-size: 7px; line-height: 8.2px; font-style: normal; }
  .env-10 { width: 430px; height: 186px; }
  .env-booklet { width: 429px; height: 294px; }
  .address-window {
    position: absolute; left: 26px; top: 129px; width: 207px; height: 37px; border-radius: 7px;
    background: linear-gradient(120deg,#b9babc 0%,#e9e9ea 30%,#a9aaad 45%,#d7d8d9 65%,#f4f4f4 80%,#bfc0c2 100%);
  }
  .envelope-back .flap { position: absolute; left: 0; top: 0; width: 100%; height: 56px; }
  .envelope-back .brand { left: 50%; transform: translateX(-50%); top: 18px; font-size: 15px; }
</style>
</head>
<body>

<svg width="0" height="0" style="position:absolute">
  <defs>
    <symbol id="icon-phone" viewBox="0 0 10 10"><path d="M1 3 Q5 -1 9 3 L7.5 4.5 L6.5 3.5 H3.5 L2.5 4.5 Z M2.5 5 H7.5 L8.5 9 H1.5 Z"/></symbol>
    <symbol id="icon-mail" viewBox="0 0 10 10"><circle cx="5" cy="5" r="5"/><path d="M2.5 3.5 H7.5 V6.8 H2.5 Z M2.5 3.5 L5 5.5 L7.5 3.5" fill="none" stroke="#fff" stroke-width="0.8"/></symbol>
    <symbol id="icon-web" viewBox="0 0 10 10"><circle cx="5" cy="5" r="5"/><path d="M1 5 H9 M5 1 Q2.5 5 5 9 Q7.5 5 5 1" fill="none" stroke="#fff" stroke-width="0.8"/></symbol>
  </defs>
</svg>

<!-- Letterhead with letter -->
<section class="sheet letter" style="left:54px; top:74px;">
  <div class="header-band" role="img" aria-label="Brand header band"></div>
  <div class="header-rule"></div>
  <div class="brand"><span class="brand-dot"></span><span class="brand-name">PEXUMOR LABS</span></div>
  <div class="letter-body">
    <p class="salutation">Dear Mr. Dalton,</p>
    <p class="paragraph">Lorem ipsum dolor sit amet, consectetuer adipiscing elit, sed diam nonmmy nibh euismod tincidunt ut laor eet dolore magna aliquam erat volutpat. Ut wisi enim ad minim veniam, quis nostrud exerci tationmcorper suscipit lobortis nisl ut aliquip ex ea commodo consequat. Duis autem vel eum iriure dolor in hendrerit in vulputate velit esse molestie consequat, vel illum dolore eu feugiat</p>
    <p class="paragraph">Rorem ipsum dolor sit amet, consectetuer adipiscing elit, sed diam nonmmy nibh euismod tincidunt ut laor eet dolore magna aliquam erat volutpat. Ut wisi enim ad minim veniam, quis nostrud exerci tationmcorper suscipit lobortis nisl ut aliquip ex ea commodo consequat. Duis autem vel eum iriure dolor in hendrerit in vulputate velit esse molest</p>
    <p class="paragraph">Dorem ipsum dolor sit amet, consectetuer adipiscing elit, sed diam nonmmy nibh euismod tincidunt ut laor eet dolore magna aliquam erat volutpat. Ut wisi enim ad minim veniam, quis nostrud exerci tationmcorper suscipit lobortis nisl ut aliquip ex ea commodo consequat. Duis autem vel eum iriure dolor in hendrerit in suscipit lobortis nisl ut aliquip ex ea commodo consequat. Duis autem vel eum iriure dolor in hendrerit in vulputate velit esse molestie consequat, vel illum</p>
    <p class="paragraph">Sorem ipsum dolor sit amet, consectetuer adipiscing elit, sed diam nonmmy nibh euismod tincidunt ut laor eet dolore magna aliquam erat volutpat. Ut wisi enim ad minim veniam, quis nostrud exerci tationmcorper suscipit lobortis nisl ut aliquip ex ea commodo consequat. Duis autem vel eum iriure dolor in</p>
    <p class="closing">Sincerely,</p>
    <div class="signature" role="img" aria-label="Handwritten signature"></div>
  </div>
  <footer class="footer">
    <div class="footer-address">4817 N. Corwin Street, Phoenix, AZ 85021</div>
    <div class="footer-contact">
      <span class="contact-item"><svg class="icon"><use href="#icon-phone"/></svg>(602)-417-3926</span>
      <span class="contact-item"><svg class="icon"><use href="#icon-mail"/></svg>information@pexumor.com</span>
      <span class="contact-item"><svg class="icon"><use href="#icon-web"/></svg>www.pexumor.com</span>
    </div>
  </footer>
</section>

<!-- Blank letterhead -->
<section class="sheet letter" style="left:395px; top:74px;">
  <div class="header-band" role="img" aria-label="Brand header band"></div>
  <div class="header-rule"></div>
  <div class="brand"><span class="brand-dot"></span><span class="brand-name">PEXUMOR LABS</span></div>
  <footer class="footer">
    <div class="footer-address">4817 N. Corwin Street, Phoenix, AZ 85021</div>
    <div class="footer-contact">
      <span class="contact-item"><svg class="icon"><use href="#icon-phone"/></svg>(602)-417-3926</span>
      <span class="contact-item"><svg class="icon"><use href="#icon-mail"/></svg>information@pexumor.com</span>
      <span class="contact-item"><svg class="icon"><use href="#icon-web"/></svg>www.pexumor.com</span>
    </div>
  </footer>
</section>

<!-- Half letter -->
<section class="sheet half-letter" style="left:734px; top:167px;">
  <div class="header-band" role="img" aria-label="Brand header band"></div>
  <div class="header-rule"></div>
  <div class="brand"><span class="brand-dot"></span><span class="brand-name">PEXUMOR LABS</span></div>
  <footer class="footer">
    <div class="footer-address">4817 N. Corwin Street, Phoenix, AZ 85021</div>
    <div class="footer-contact">
      <span class="contact-item"><svg class="icon"><use href="#icon-phone"/></svg>(602)-417-3926</span>
      <span class="contact-item"><svg class="icon"><use href="#icon-mail"/></svg>information@pexumor.com</span>
      <span class="contact-item"><svg class="icon"><use href="#icon-web"/></svg>www.pexumor.com</span>
    </div>
  </footer>
</section>

<!-- #10 envelope -->
<section class="sheet envelope env-10" style="left:54px; top:507px;">
  <div class="header-band" role="img" aria-label="Brand header band"></div>
  <div class="header-rule"></div>
  <div class="brand"><span class="brand-dot"></span><span class="brand-name">PEXUMOR LABS</span></div>
  <address class="return-address">4817 N. Corwin Street<br>Phoenix, AZ 85021</address>
</section>

<!-- Booklet envelope -->
<section class="sheet envelope env-booklet" style="left:509px; top:507px;">
  <div class="header-band" role="img" aria-label="Brand header band"></div>
  <div class="header-rule"></div>
  <div class="brand"><span class="brand-dot"></span><span class="brand-name">PEXUMOR LABS</span></div>
  <address class="return-address">4817 N. Corwin Street<br>Phoenix, AZ 85021</address>
</section>

<!-- #10 window envelope -->
<section class="sheet envelope env-10" style="left:54px; top:724px;">
  <div class="header-band" role="img" aria-label="Brand header band"></div>
  <div class="header-rule"></div>
  <div class="brand"><span class="brand-dot"></span><span class="brand-name">PEXUMOR LABS</span></div>
  <address class="return-address">4817 N. Corwin Street<br>Phoenix, AZ 85021</address>
  <div class="address-window"></div>
</section>

<!-- #10 envelope back -->
<section class="sheet envelope-back env-10" style="left:54px; top:939px;">
  <svg class="flap" viewBox="0 0 430 56" preserveAspectRatio="none">
    <path d="M0,0 H430 L420,38 Q415,51 398,51 H32 Q15,51 10,38 Z" fill="#fff" stroke="#d4d4d4" stroke-width="2"/>
  </svg>
  <div class="brand"><span class="brand-dot"></span><span class="brand-name">PEXUMOR LABS</span></div>
</section>

<!-- Open end envelope back -->
<section class="sheet envelope-back env-booklet" style="left:509px; top:832px;">
  <svg class="flap" viewBox="0 0 429 56" preserveAspectRatio="none">
    <path d="M0,0 H429 L419,38 Q414,51 397,51 H32 Q15,51 10,38 Z" fill="#fff" stroke="#d4d4d4" stroke-width="2"/>
  </svg>
  <div class="brand"><span class="brand-dot"></span><span class="brand-name">PEXUMOR LABS</span></div>
</section>

</body>
</html>
```